Pizza Box 10" x 10" - color: White

Custom design, utilizing CrustLoomo Logo and include the following information on the Pizza Box:

1. Custom Crafted Pizza with Quality Ingredients.
2. [....Get Your GAME ON] to be placed on the front flap and seen when the
box is opened.
3. You"ll miss 100% of the Pizza you don't eat.

4. Visit www.fennelcartonworks.example for additional design resource information. Go to site and then click on ORDERING to access.

5. The 10" x 10" Pizza Box is to be in the color WHITE.
6. Use colors Black and Red. no generic images. no food pics. I am looking for a clean and cool design.

Target Market(s)

Age 16 - 36 years

Industry/Entity Type

American Restaurant

Font styles to use
Sans Serif

Colors
ec1f27
000000
ffffff

Requirements
Must have
• Color Red and Black.
• Logo on Top and all sides of the Pizza Box.
Nice to have
• A Creative design that does not look generic.
Should not have
• No food images.

```html
<!DOCTYPE html>
<html lang="en">
<head>
<meta charset="utf-8">
<title>CrustLoomo 10 x 10 Pizza Box Dieline</title>
<link rel="stylesheet" href="https://fonts.googleapis.com/css2?family=Oswald:wght@400;500&family=Montserrat:wght@600;700&display=swap">
<style>
  :root {
    --brand-red: #ec1f27;
    --brand-black: #000000;
    --board-white: #ffffff;
    --backdrop: #5b5b5b;
    --cut-line: #8a8a8a;
    --fold-line: #444444;
  }
  html, body {
    margin: 0;
    width: 720px;
    height: 1200px;
    overflow: hidden;
    background: var(--backdrop);
  }
  .dieline { display: block; width: 720px; height: 1200px; }
  .board { fill: var(--board-white); stroke: var(--cut-line); stroke-width: 1.5; }
  .fold { fill: none; stroke: var(--fold-line); stroke-width: 1.2; stroke-dasharray: 7 6; }
  .band-red { fill: var(--brand-red); stroke: var(--brand-black); stroke-width: 3; }
  .band-black { fill: var(--brand-black); }
  .slogan { font-family: "Oswald", sans-serif; font-weight: 400; fill: var(--board-white); letter-spacing: 0.5px; }
  .wordmark { font-family: "Oswald", sans-serif; font-weight: 500; }
  .wordmark-black { fill: var(--brand-black); }
  .wordmark-white { fill: var(--board-white); }
  .mark-dot { fill: none; stroke-width: 4; }
  .lid-frame { fill: var(--board-white); stroke: var(--brand-black); stroke-width: 3; }
  .hero-band { fill: var(--brand-red); }
  .hero-kicker { font-family: "Montserrat", sans-serif; font-weight: 600; fill: var(--board-white); }
  .hero-title { font-family: "Montserrat", sans-serif; font-weight: 700; fill: var(--board-white); }
</style>
</head>
<body>
<svg class="dieline" viewBox="0 0 900 1500" xmlns="http://www.w3.org/2000/svg">
  <defs>
    <radialGradient id="badge-tone" cx="50%" cy="50%" r="50%">
      <stop offset="0%" stop-color="#000" stop-opacity="1"/>
      <stop offset="45%" stop-color="#000" stop-opacity="0.95"/>
      <stop offset="75%" stop-color="#000" stop-opacity="0.35"/>
      <stop offset="100%" stop-color="#000" stop-opacity="0"/>
    </radialGradient>
    <clipPath id="hero-panel-clip"><rect x="217" y="897" width="454" height="454"/></clipPath>
  </defs>

  <!-- box outline -->
  <g class="board-shape">
    <path class="board" d="M180,20 L192,10 L360,10 L372,20 L520,20 L532,10 L700,10 L710,20 L710,235 L180,235 Z"/>
    <path class="board" d="M85,20 L170,20 L172,120 Q180,130 188,120 L188,235 L85,235 Z"/>
    <path class="board" d="M805,20 L720,20 L718,120 Q710,130 702,120 L702,235 L805,235 Z"/>
    <rect class="board" x="85" y="235" width="720" height="525"/>
    <path class="board" d="M180,760 L710,760 L710,850 L695,865 L195,865 L180,850 Z"/>
    <path class="board" d="M85,760 L180,760 L180,850 L190,865 L85,895 Z"/>
    <path class="board" d="M805,760 L710,760 L710,850 L700,865 L805,895 Z"/>
    <path class="board" d="M85,895 L190,865 L700,865 L805,895 L805,1210 L785,1230 L805,1260 L805,1365 L785,1385 L105,1385 L85,1365 L85,1260 L105,1230 L85,1210 Z"/>
    <path class="board" d="M190,1385 L700,1385 L700,1475 L685,1490 L205,1490 L190,1475 Z"/>
  </g>

  <!-- fold lines -->
  <g class="folds">
    <path class="fold" d="M190,128 L418,128 M468,128 L700,128"/>
    <circle cx="443" cy="123" r="25" fill="#fff" stroke="#444" stroke-width="1.2"/>
    <path class="fold" d="M183,240 L183,760 M707,240 L707,760"/>
    <path class="fold" d="M190,870 L190,1380 M698,870 L698,1380"/>
  </g>

  <!-- top tuck flap slogan -->
  <rect class="band-red" x="215" y="161" width="458" height="51"/>
  <text class="slogan" x="440" y="194" font-size="21" text-anchor="middle">YOU'LL MISS 100% OF THE PIZZA YOU DON'T EAT.</text>

  <!-- lid side bars -->
  <rect class="band-red" x="108" y="268" width="52" height="458"/>
  <g transform="translate(134,500) rotate(90)">
    <circle class="mark-dot" cx="-62" cy="-6" r="11" stroke="#fff"/>
    <text class="wordmark wordmark-white" x="-44" y="2" font-size="22">CrustLoomo</text>
  </g>
  <rect class="band-red" x="727" y="268" width="52" height="458"/>
  <g transform="translate(753,497) rotate(-90)">
    <circle class="mark-dot" cx="-62" cy="-6" r="11" stroke="#fff"/>
    <text class="wordmark wordmark-white" x="-44" y="2" font-size="22">CrustLoomo</text>
  </g>

  <!-- lid centre name -->
  <circle class="mark-dot" cx="280" cy="493" r="45" stroke="#000" stroke-width="6"/>
  <text class="wordmark wordmark-black" x="346" y="515" font-size="66">CrustLoomo</text>

  <!-- front panel -->
  <rect class="band-red" x="215" y="786" width="458" height="50"/>
  <g transform="translate(565,811) rotate(180)">
    <circle class="mark-dot" cx="-78" cy="-7" r="17" stroke="#fff"/>
    <text class="wordmark wordmark-white" x="-52" y="4" font-size="28">CrustLoomo</text>
  </g>

  <!-- base side bars -->
  <rect class="band-black" x="125" y="897" width="38" height="456"/>
  <g transform="translate(144,1130) rotate(90)">
    <circle class="mark-dot" cx="-62" cy="-6" r="10" stroke="#fff" stroke-width="3"/>
    <text class="wordmark wordmark-white" x="-46" y="1" font-size="20">CrustLoomo</text>
  </g>
  <rect class="band-black" x="726" y="897" width="38" height="456"/>
  <g transform="translate(745,1128) rotate(-90)">
    <circle class="mark-dot" cx="-62" cy="-6" r="10" stroke="#fff" stroke-width="3"/>
    <text class="wordmark wordmark-white" x="-46" y="1" font-size="20">CrustLoomo</text>
  </g>

  <!-- base hero panel -->
  <rect class="lid-frame" x="215" y="895" width="458" height="458"/>
  <g clip-path="url(#hero-panel-clip)">
    <rect class="hero-band" x="217" y="1056" width="454" height="157"/>
    <ellipse role="img" aria-label="Badge artwork: black burst with rays and red rings behind the pizza headline" cx="440" cy="1125" rx="200" ry="200" fill="url(#badge-tone)"/>
  </g>
  <text class="hero-kicker" x="444" y="1072" font-size="18" text-anchor="middle">CUSTOM CRAFTED</text>
  <text class="hero-title" x="444" y="1158" font-size="70" text-anchor="middle">Pizza</text>
  <text class="hero-kicker" x="444" y="1198" font-size="20" text-anchor="middle">with Quality</text>
  <text class="hero-kicker" x="444" y="1228" font-size="13" text-anchor="middle">INGREDIENTS</text>

  <circle class="mark-dot" cx="250" cy="1325" r="17" stroke="#000" stroke-width="4"/>
  <text class="wordmark wordmark-black" x="278" y="1337" font-size="30">CrustLoomo</text>

  <!-- front flap message -->
  <rect class="band-black" x="215" y="1414" width="458" height="38"/>
  <text class="slogan" x="436" y="1442" font-size="25" text-anchor="middle">....GET YOUR GAME ON</text>
</svg>
</body>
</html>
```